LET ME HANDLE YOUR AUCTION NEEDS!

I am here to handle all your auction needs, I have over 20 years of auction experience buying and selling for dealerships in North Carolina and Tennessee. Send me to the sale to either rep your vehicles or let me know what you need and I can be
another set of eyes to help you buy what is hot and bad credit cars are my specialty. You know a car always sells better with a familiar face rather than auction personnel and with my great reputation I will be able to help find the buyers for your aged inventory.
Call me today and let's get started.
Rick Halvorsen 555-862-3917
(please have pictures of vehicles or an auto auction in the design)

```html
<!DOCTYPE html>
<html lang="en">
<head>
<meta charset="utf-8">
<title>Rick Halvorsen – Auction Postcard</title>
<link href="https://fonts.googleapis.com/css2?family=Fjalla+One&family=Oswald:wght@300;400&family=Jost:wght@400&display=swap" rel="stylesheet">
<style>
  :root {
    --stage: #2a2a2a;
    --yellow: #ffe600;
    --white: #ffffff;
    --ink: #1d1d1d;
    --blue-deep: #1d7ac4;
    --blue-mid: #2f8fd6;
    --blue-light: #4ac7ec;
    --fold: #8ba6d9;
    --rule: #8a8a8a;
  }
  * { margin: 0; padding: 0; box-sizing: border-box; }
  html, body { width: 900px; height: 1200px; overflow: hidden; }
  body { background: var(--stage); position: relative; font-family: "Jost", sans-serif; }

  .postcard { position: absolute; left: 77px; width: 747px; height: 536px; overflow: hidden; }
  .postcard--front { top: 37px; }
  .postcard--back { top: 622px; background: var(--white); }

  .hero-photo {
    position: absolute; inset: 0;
    background:
      radial-gradient(ellipse at 30% 40%, rgba(90,110,140,.55), transparent 60%),
      radial-gradient(ellipse at 80% 30%, rgba(210,200,190,.6), transparent 55%),
      linear-gradient(160deg, #2e3f5a 0%, #4b5a70 40%, #a99a8a 70%, #1d2230 100%);
  }
  .headline {
    position: absolute; left: 47px; top: 34px;
    font-family: "Fjalla One", sans-serif; font-size: 38px; line-height: 52px;
    color: var(--yellow); text-transform: uppercase; letter-spacing: .2px;
  }
  .intro {
    position: absolute; left: 45px; top: 150px; width: 400px;
    font-size: 18px; line-height: 24px; color: var(--white);
  }
  .front-cta { position: absolute; right: 62px; top: 448px; text-align: right; font-family: "Fjalla One", sans-serif; }
  .front-cta__lead { font-size: 29px; color: var(--white); line-height: 40px; }
  .front-cta__contact { font-size: 29px; color: var(--yellow); line-height: 40px; display: flex; align-items: center; gap: 8px; justify-content: flex-end; }

  .back-panel { position: absolute; inset: 0; }
  .back-copy {
    position: absolute; left: 43px; top: 40px; width: 325px;
    font-size: 18px; line-height: 24.6px; color: var(--ink);
  }
  .back-copy p + p { margin-top: 24.6px; }
  .ribbon-text { position: absolute; left: 40px; top: 372px; width: 395px; font-family: "Oswald", sans-serif; color: var(--white); }
  .ribbon-text__lead { font-weight: 300; font-size: 22px; line-height: 34px; letter-spacing: .1px; white-space: nowrap; }
  .ribbon-text__contact { font-weight: 400; font-size: 30px; line-height: 46px; display: flex; align-items: center; gap: 5px; white-space: nowrap; }
  .ribbon-text__contact .phone-icon { width: 22px; height: 22px; }

  .stamp-box { position: absolute; left: 626px; top: 36px; width: 85px; height: 93px; border: 1px solid #444; }
  .address-line { position: absolute; left: 494px; width: 217px; height: 1px; background: var(--rule); }
  .phone-icon { width: 24px; height: 24px; flex: none; }
</style>
</head>
<body>
  <section class="postcard postcard--front">
    <div class="hero-photo" role="img" aria-label="Photo of a handshake and car keys being handed over in front of a car at an auto auction"></div>
    <h1 class="headline">I am here to handle<br>all your auction needs</h1>
    <p class="intro">I have over 20 years of auction experience buying and selling for dealerships in North Carolina and Tennessee</p>
    <div class="front-cta">
      <div class="front-cta__lead">Call me today</div>
      <div class="front-cta__contact">Rick Halvorsen
        <svg class="phone-icon" viewBox="0 0 24 24"><circle cx="12" cy="12" r="10" fill="none" stroke="currentColor" stroke-width="2"/><path d="M8.5 7c.6-.5 1.3-.4 1.6.2l.8 1.6c.2.5 0 1-.4 1.3l-.6.4c.5 1.3 1.4 2.3 2.6 2.9l.5-.6c.3-.4.9-.5 1.3-.3l1.6.9c.6.3.6 1 .2 1.5-1 1.1-2.4 1.2-4 .3-2-1.2-3.5-3-4.2-5.2-.4-1.2-.2-2.3.6-3z" fill="currentColor"/></svg>
        555-862-3917</div>
    </div>
  </section>

  <section class="postcard postcard--back">
    <svg class="back-panel" viewBox="0 0 747 536" aria-hidden="true">
      <defs>
        <linearGradient id="panelBlue" x1="0" y1="0" x2="1" y2="1">
          <stop offset="0" stop-color="#2f8fd6"/>
          <stop offset="1" stop-color="#4ac7ec"/>
        </linearGradient>
      </defs>
      <polygon points="0,0 458,0 403,363 468,536 0,536" fill="url(#panelBlue)"/>
      <polygon points="440,363 463,363 463,450 440,461" fill="#8ba6d9"/>
      <rect x="0" y="363" width="440" height="98" fill="#1d7ac4"/>
    </svg>
    <div class="back-copy">
      <p>Send me to the sale to either rep your vehicles or let me know what you need and I can be another set of eyes to help you buy what is hot and bad credit cars are my specialty.</p>
      <p>You know a car always sells better with a familiar face rather than auction personnel and with my great reputation I will be able to help find the buyers for your aged inventory.</p>
    </div>
    <div class="ribbon-text">
      <div class="ribbon-text__lead">CALL ME TODAY AND LET'S GET STARTED.</div>
      <div class="ribbon-text__contact">RICK HALVORSEN
        <svg class="phone-icon" viewBox="0 0 24 24"><circle cx="12" cy="12" r="10" fill="none" stroke="currentColor" stroke-width="2"/><path d="M8.5 7c.6-.5 1.3-.4 1.6.2l.8 1.6c.2.5 0 1-.4 1.3l-.6.4c.5 1.3 1.4 2.3 2.6 2.9l.5-.6c.3-.4.9-.5 1.3-.3l1.6.9c.6.3.6 1 .2 1.5-1 1.1-2.4 1.2-4 .3-2-1.2-3.5-3-4.2-5.2-.4-1.2-.2-2.3.6-3z" fill="currentColor"/></svg>
        555-862-3917</div>
    </div>
    <div class="stamp-box"></div>
    <div class="address-line" style="top:321px"></div>
    <div class="address-line" style="top:358px"></div>
    <div class="address-line" style="top:395px"></div>
  </section>
</body>
</html>
```